20 Inspiring Instagram posts about marketing

Create me 15 inspiring Instagram posts about marketing and branding. The tips need to be original and inspiring so is the design. Can turn into a long time project on all social media channels in the future.

```html
<!DOCTYPE html>
<html lang="en">
<head>
<meta charset="UTF-8">
<title>Make Your Marketing So Useful</title>
<link rel="stylesheet" href="https://fonts.googleapis.com/css2?family=Montserrat:wght@300;400;700&display=swap">
<style>
  :root {
    --frame: #2d3e50;
    --panel: #1b2534;
    --ink: #ffffff;
    --ring: #c9c9c9;
    --gold: #d9cc5c;
  }
  html, body {
    margin: 0;
    padding: 0;
    width: 1200px;
    height: 1200px;
    overflow: hidden;
    background: var(--frame);
  }
  .post {
    width: 1200px;
    height: 1200px;
    display: block;
  }
  .quote-text {
    font-family: "Montserrat", sans-serif;
    fill: var(--ink);
    text-anchor: middle;
  }
  .quote-text--light { font-weight: 300; font-size: 64px; }
  .quote-text--bold { font-weight: 700; font-size: 72px; }
  .brush-ring {
    fill: none;
    stroke: var(--ring);
    stroke-width: 18;
    stroke-linecap: round;
  }
  .brand-ring {
    fill: none;
    stroke: var(--gold);
    stroke-width: 4;
  }
  .brand-name {
    font-family: "Montserrat", sans-serif;
    font-weight: 400;
    font-size: 24px;
    fill: var(--gold);
    text-anchor: middle;
  }
</style>
</head>
<body>
<svg class="post" viewBox="0 0 1200 1200" xmlns="http://www.w3.org/2000/svg" role="img" aria-label="Make your marketing so useful people would pay for it">
  <rect class="panel" x="24" y="24" width="1152" height="1152" fill="var(--panel)"/>

  <path class="brush-ring" d="M206 356 A467 467 0 1 1 149 728"/>

  <text class="quote-text quote-text--light" x="586" y="367" textLength="489" lengthAdjust="spacingAndGlyphs">MAKE YOUR</text>
  <text class="quote-text quote-text--bold" x="577" y="473" textLength="780" lengthAdjust="spacing">MARKETING</text>
  <text class="quote-text quote-text--light" x="574" y="580" textLength="400" lengthAdjust="spacingAndGlyphs">SO USEFUL</text>
  <text class="quote-text quote-text--bold" x="582" y="690" textLength="597" lengthAdjust="spacing">PEOPLE</text>
  <text class="quote-text quote-text--light" x="577" y="795" textLength="780" lengthAdjust="spacingAndGlyphs">WOULD PAY FOR IT</text>

  <g class="brand-mark">
    <circle class="brand-ring" cx="600" cy="907" r="94"/>
    <text class="brand-name" x="600" y="899">LENA R.</text>
    <text class="brand-name" x="600" y="933">VALE</text>
  </g>
</svg>
</body>
</html>
```